Business Card Design Project

New business cards that encompass our new logo.
Looking for -
Name, Title, Cell Phone, Email, Address (2 lines), Main Phone, Fax, and website.
Reason: I don't like the graphics used to show phone, fax, cell, email, web, and address.....
I like the double sided cards with logo's on the back. I do not like the logos for phone, fax, cell, address, email, or web.

```html
<!DOCTYPE html>
<html lang="en">
<head>
<meta charset="utf-8">
<title>Northpeak Restaurant Supply – Business Card</title>
<link href="https://fonts.googleapis.com/css2?family=Montserrat:wght@400;600;700&display=swap" rel="stylesheet">
<style>
  :root {
    --navy: #1d4489;
    --red: #cf3a48;
    --white: #ffffff;
    --ink: #555a60;
    --steel-light: #e6e8ea;
    --steel-dark: #8d9297;
    --stage: #e9eaec;
  }
  * { margin: 0; padding: 0; box-sizing: border-box; }
  html, body {
    width: 1200px; height: 1000px; overflow: hidden;
    background: var(--stage);
    font-family: "Montserrat", Arial, sans-serif;
  }
  .sheet {
    width: 1200px; height: 1000px;
    display: flex; align-items: center; justify-content: center; gap: 50px;
  }
  .card {
    position: relative; width: 520px; height: 300px;
    background: var(--white); overflow: hidden;
    box-shadow: 0 6px 18px rgba(0,0,0,.18);
  }
  .photo {
    position: absolute;
    background: linear-gradient(135deg, var(--steel-light) 0%, #b9bdc1 45%, var(--steel-dark) 100%);
  }
  /* front */
  .front .photo { right: 0; top: 0; width: 230px; height: 230px; }
  .front .band {
    position: absolute; left: 0; top: 22px; width: 100%; height: 100px;
    background: var(--navy);
  }
  .front .identity { position: absolute; left: 26px; top: 66px; }
  .front .name { color: var(--red); font-size: 21px; font-weight: 600; }
  .front .title { color: var(--white); font-size: 13px; font-weight: 400; margin-top: 2px; }
  .front .direct {
    position: absolute; right: 22px; top: 36px; text-align: left;
    color: var(--white); font-size: 13px; line-height: 1.35;
  }
  .front .direct .cell { font-weight: 600; font-size: 14px; }
  .front .address {
    position: absolute; left: 26px; bottom: 34px;
    color: var(--ink); font-size: 13px; line-height: 1.45;
  }
  /* back */
  .back .photo { left: 0; top: 0; width: 175px; height: 100%; }
  .back .brand {
    position: absolute; left: 175px; right: 0; top: 90px; text-align: center;
    color: var(--navy); font-weight: 700; line-height: 1.15;
  }
  .back .brand-name { font-size: 40px; letter-spacing: 1px; }
  .back .brand-line { font-size: 15px; letter-spacing: 2px; margin-top: 4px; }
  .back .website {
    position: absolute; left: 175px; right: 0; bottom: 30px; text-align: center;
    color: var(--ink); font-size: 14px;
  }
</style>
</head>
<body>
<main class="sheet">
  <section class="card front">
    <div class="photo" role="img" aria-label="Photo of a stainless steel commercial kitchen line"></div>
    <div class="band"></div>
    <div class="identity">
      <p class="name">Dana Whitfield</p>
      <p class="title">Accountant</p>
    </div>
    <div class="direct">
      <p class="cell">070 555 0142</p>
      <p class="email">hello@northpeak.com</p>
    </div>
    <div class="address">
      <p>48 Harbour Lane</p>
      <p>Westfield Bristol BS7</p>
      <p>T+ 84 5550 1200</p>
      <p>F+ 84 5550 1288</p>
    </div>
  </section>

  <section class="card back">
    <div class="photo" role="img" aria-label="Photo of a stainless steel commercial kitchen"></div>
    <div class="brand">
      <p class="brand-name">NORTHPEAK</p>
      <p class="brand-line">RESTAURANT SUPPLY</p>
    </div>
    <p class="website">www.northpeak.com</p>
  </section>
</main>
</body>
</html>
```